I need the below text put into an illustration/high res image so I can print out and frame and give to my fiance. Can be simple but must look elegant. Idea is that the text can be written in the sand on the attached pics (let me know if you require more high res). Not precious on the dimensions but think no more than 90cm length or width. Can be smaller whatever you think works best. You can half long sentences if you think it will look better.
Update: some of you asked for a picture of us, not sure it works but have attached one
Marriage
Marriage isn’t for you.
You don’t marry to make yourself happy, you marry to make someone else happy.
More than that, your marriage isn’t for yourself, you’re marrying for a family.
Not just for the in-laws and all of that nonsense, but for your future children.
Who do you want to help you raise them?
Who do you want to influence them?
Marriage isn’t for you.
It’s not about you.
Marriage is about the person you married.

```html
<!DOCTYPE html>
<html lang="en">
<head>
<meta charset="utf-8">
<title>Marriage</title>
<link rel="stylesheet" href="https://fonts.googleapis.com/css2?family=Pinyon+Script&display=swap">
<style>
  :root {
    --ink: #1f3a1c;
    --sky: #e4edf2;
    --sea-far: #b7ccd6;
    --surf: #d6e3e6;
    --wet-sand: #c4c9c2;
    --sand: #bcb9a8;
    --sand-deep: #aeab99;
  }
  html, body {
    margin: 0;
    padding: 0;
    overflow: hidden;
    background: var(--sand);
  }
  .poster {
    position: relative;
    width: 1200px;
    height: 987px;
    overflow: hidden;
    font-family: "Pinyon Script", cursive;
    color: var(--ink);
  }
  .beach-backdrop {
    position: absolute;
    inset: 0;
    width: 1200px;
    height: 987px;
  }
  .poem-title {
    position: absolute;
    top: 62px;
    left: 0;
    width: 1210px;
    margin: 0;
    text-align: center;
    font-weight: 400;
    font-size: 76px;
    line-height: 1;
  }
  .poem-verses {
    position: absolute;
    top: 207px;
    left: 0;
    width: 1180px;
    margin: 0;
    text-align: center;
    font-size: 39px;
    line-height: 47.6px;
  }
  .poem-verses span { display: block; }
  .poem-closing {
    position: absolute;
    top: 888px;
    left: 0;
    width: 1190px;
    margin: 0;
    text-align: center;
    font-size: 39px;
    line-height: 47.6px;
  }
</style>
</head>
<body>
<main class="poster">
  <svg class="beach-backdrop" role="img" aria-label="Photograph of a sandy beach with waves and a headland under a pale sky, a single white rose lying on the sand" viewBox="0 0 1200 987" preserveAspectRatio="none">
    <defs>
      <linearGradient id="beach-tones" x1="0" y1="0" x2="0" y2="1">
        <stop offset="0" stop-color="var(--sky)"/>
        <stop offset="0.07" stop-color="var(--sea-far)"/>
        <stop offset="0.14" stop-color="var(--surf)"/>
        <stop offset="0.3" stop-color="var(--wet-sand)"/>
        <stop offset="0.45" stop-color="var(--sand)"/>
        <stop offset="1" stop-color="var(--sand-deep)"/>
      </linearGradient>
    </defs>
    <rect width="1200" height="987" fill="url(#beach-tones)"/>
  </svg>

  <h1 class="poem-title">Marriage</h1>

  <p class="poem-verses">
    <span>Marriage isn’t for you.</span>
    <span>You don’t marry to make yourself happy,</span>
    <span>you marry to make someone else happy.</span>
    <span>More than that, your marriage isn’t for yourself,</span>
    <span>you’re marrying for a family.</span>
    <span>Not just for the in-laws and all of that nonsense,</span>
    <span>but for your future children.</span>
    <span>Who do you want to help you raise them?</span>
    <span>Who do you want to influence them?</span>
    <span>Marriage isn’t for you.</span>
    <span>It’s not about you.</span>
  </p>

  <p class="poem-closing">Marriage is about the person you married.</p>
</main>
</body>
</html>
```